Higher $ Now Guaranteed! Redesign Web Page(s) Style Composition and Color (Graphics design-not code)

We need a modern look for an existing website. You can either use or change the current logo. Choice of colors, fonts, style is up to you. Sample URLs and additional details are provided in the attached document. Most of our struggle has been the appearance of the directory listings (city) page.
----------------------------------------------------------------------------------
--> Increased Project Budget and Now Funds are GUARANTEED
--> Added an additional attachment in response to questions
-->THIS PROJECT IS FOR GRAPHICS/DESIGN NOT CODE
The project is mostly a few areas of text and colored boxes or lines. Hopefully a skilled designer can place these elements in an attractive layout and choose the right colors and styles. There are no complex drawings required for this project.

*** We are involved with other projects from time to time and expect that the winning designer will be given the first opportunity at this future work. ***

*** There is no requirement to do any code but if you submit a design feel free to indicate if you wish to be considered for any future code work on this site or others ***

Font styles to use
Sans Serif

Requirements
Must have
• Rounded corners on images and buttons with nice gradients or hover effects.
Nice to have
• Attached an additional descriptions document to help with these answers.
Should not have
• Small fonts, traditional older looking rectangular buttons, dull or boring color schemes

```html
<!DOCTYPE html>
<html lang="en">
<head>
<meta charset="utf-8">
<title>LedgerLocate – Find the Best Tax Professionals</title>
<link href="https://fonts.googleapis.com/css2?family=Raleway:wght@400;500;600;700&display=swap" rel="stylesheet">
<style>
:root{
  --ink:#1b2a30;
  --ink-soft:#2a2f33;
  --text-dark:#2c2c34;
  --white:#ffffff;
  --sky:#86cdee;
  --orange-1:#ffa43a;
  --orange-2:#f2780f;
  --purple-1:#b46ab8;
  --purple-2:#7f2f86;
  --card:rgba(176,120,220,.55);
  --line-orange:#f7941d;
  --line-red:#d1245a;
  --line-purple:#8e2d8e;
  --line-yellow:#f3d21c;
  --line-green:#8cc63f;
  --line-blue:#29a8e0;
  --footer-text:#c9d0d3;
  --muted:#7c8286;
}
*{box-sizing:border-box;margin:0;padding:0}
html,body{width:1200px;height:773px;overflow:hidden;background:var(--white)}
body{position:relative;font-family:'Raleway',Arial,sans-serif;color:var(--text-dark)}
.hero-photo{position:absolute;left:0;top:0;width:1200px;height:610px;
  background:linear-gradient(120deg,#e9dcd6 0%,#d9c3cf 25%,#c9b3d6 45%,#d7c6e4 60%,#b9a6cf 80%,#cdb8d8 100%)}
.site-header{position:absolute;left:0;top:0;width:1200px;height:66px;background:rgba(255,255,255,.72)}
.brand{position:absolute;left:245px;top:19px;display:flex;align-items:center;gap:6px;font-size:18px;font-weight:600;color:var(--ink-soft)}
.brand-dot{width:12px;height:12px;border-radius:50%;background:var(--ink-soft)}
.main-nav{position:absolute;left:518px;top:38px;display:flex;font-size:12px;color:var(--ink-soft)}
.main-nav a{color:inherit;text-decoration:none;padding:0 10px;border-left:1px solid #9a9a9a;line-height:14px}
.main-nav a:first-child{border-left:0}
.phone{position:absolute;left:848px;top:36px;display:flex;align-items:center;gap:4px;font-size:15px;font-weight:600;color:var(--ink-soft)}
.rainbow{position:absolute;left:0;width:1200px;height:3px;display:flex}
.rainbow span{height:100%}
.rainbow .o{width:235px;background:var(--line-orange)}
.rainbow .r{width:120px;background:var(--line-red)}
.rainbow .p{width:107px;background:var(--line-purple)}
.rainbow .y{width:138px;background:var(--line-yellow)}
.rainbow .g{width:115px;background:var(--line-green)}
.rainbow .b{flex:1;background:var(--line-blue)}
.hero-title{position:absolute;left:0;width:1200px;top:95px;text-align:center;font-size:18px;font-weight:700;letter-spacing:.4px;color:var(--text-dark)}
.hero-sub{position:absolute;left:0;width:1200px;top:122px;text-align:center;font-size:11px;color:#3b3b44}
.search-bar{position:absolute;left:240px;top:158px;width:720px;height:42px;background:var(--sky)}
.field{position:absolute;top:10px;height:22px;background:var(--white);border:1px solid #d4d4d4;border-radius:3px;font-size:9px;color:#9a9a9a;padding:6px 6px 0}
.field svg{position:absolute;right:6px;top:7px}
.field.state{left:20px;width:140px}
.field.city{left:188px;width:140px}
.field.zip{left:393px;width:140px}
.or{position:absolute;left:349px;top:12px;font-size:15px;font-weight:600;color:var(--white)}
.btn-search{position:absolute;left:561px;top:10px;width:140px;height:22px;border-radius:3px;background:linear-gradient(var(--orange-1),var(--orange-2));color:var(--white);font-size:11px;font-weight:600;text-align:center;line-height:23px}
.us-map{position:absolute;left:455px;top:225px;width:290px;height:180px;border-radius:8px;background:linear-gradient(160deg,#2b3840,#1b262c)}
.cta-card{position:absolute;left:793px;top:267px;width:167px;height:95px;background:var(--card);text-align:center}
.cta-card h3{font-size:8px;font-weight:700;margin-top:12px;color:#1d1d26}
.cta-card p{font-size:6px;line-height:8px;margin:8px 8px 0;color:#2e2e3a}
.btn-listed{position:absolute;left:13px;top:66px;width:140px;height:22px;border-radius:4px;background:linear-gradient(var(--purple-1),var(--purple-2));color:var(--white);font-size:11px;font-weight:500;line-height:22px}
.about-head{position:absolute;left:0;top:427px;width:1200px;height:28px;background:var(--ink);color:var(--white);text-align:center;font-size:14px;font-weight:600;line-height:28px}
.about-body{position:absolute;left:0;top:455px;width:1200px;height:155px;background:rgba(35,30,32,.78)}
.about-body p{width:440px;margin:29px auto 0;text-align:center;font-size:8.6px;line-height:10.4px;color:var(--white)}
.about-body p + p{margin-top:10px}
.site-footer{position:absolute;left:0;top:613px;width:1200px;height:122px;background:var(--ink)}
.foot-col{position:absolute;top:26px;font-size:11px;color:var(--footer-text);line-height:15px}
.foot-col h4{font-size:11px;font-weight:700;letter-spacing:.4px;margin-bottom:15px;color:var(--footer-text)}
.foot-col.nav{left:240px}
.foot-col.contact{left:441px}
.foot-col.legal{left:635px}
.foot-divider{position:absolute;top:9px;width:1px;height:103px;background:#6f7a7e}
.foot-brand{position:absolute;left:860px;top:50px;display:flex;align-items:center;gap:5px;font-size:15px;font-weight:600;color:#5d686c}
.foot-brand span.dot{width:10px;height:10px;border-radius:50%;background:#5d686c}
.copyright{position:absolute;left:0;top:747px;width:1146px;text-align:center;font-size:11px;color:var(--muted)}
</style>
</head>
<body>
<div class="hero-photo" role="img" aria-label="Soft-focus desk photo with glasses, a calculator, a coffee cup and a notepad about taxes"></div>

<header class="site-header">
  <div class="brand"><span class="brand-dot"></span>LedgerLocate</div>
  <nav class="main-nav"><a href="#">Home</a><a href="#">Get Listed</a><a href="#">Contact Us</a><a href="#">Members Login</a></nav>
  <div class="phone">
    <svg width="12" height="14" viewBox="0 0 12 14"><path d="M2 1l2.5-.5 1.5 3.5-1.6 1.2c.6 1.8 1.6 3 3.1 4L9 8l3 2-.6 2.6C6 13 1 7.5 2 1z" fill="#2a2f33"/></svg>
    555-014-2290
  </div>
</header>
<div class="rainbow" style="top:66px"><span class="o"></span><span class="r"></span><span class="p"></span><span class="y"></span><span class="g"></span><span class="b"></span></div>

<h1 class="hero-title">FIND THE BEST TAX PROFESSIONALS IN YOUR AREA</h1>
<p class="hero-sub">Our directories of tax professionals give you immediate access to the very best tax preparers and income tax advisors in your area.</p>

<form class="search-bar">
  <div class="field state">State<svg width="12" height="7" viewBox="0 0 12 7"><path d="M1 1l5 5 5-5" stroke="#aaa" fill="none"/></svg></div>
  <div class="field city">City<svg width="12" height="7" viewBox="0 0 12 7"><path d="M1 1l5 5 5-5" stroke="#aaa" fill="none"/></svg></div>
  <span class="or">OR</span>
  <div class="field zip">Zip Code</div>
  <div class="btn-search">SEARCH</div>
</form>

<div class="us-map" role="img" aria-label="Clickable map of the United States with state abbreviations"></div>

<aside class="cta-card">
  <h3>ARE YOU TAX PREPARER ?</h3>
  <p>Our directories of tax professionals give you immediate access to the very best tax preparers and income tax advisors in your area</p>
  <div class="btn-listed">GET LISTED</div>
</aside>

<h2 class="about-head">About LEDGERLOCATE.COM</h2>
<section class="about-body">
  <p>Lorem ipsum dolor sit amet, consectetur adipiscing elit. Morbi pulvinar at mi eu hendrerit. Sed sagittis turpis lacus, ac ultrices diam ullamcorper nec. Nulla facilisi. Sed in blandit ligula, eu laoreet ex. Ut eleifend mi eget vulputate ultricies. Suspendisse nec nibh non ligula suscipit malesuada. Mauris a urna id arcu sollicitudin laoreet.</p>
  <p>Donec rutrum velit enim, a sollicitudin nisl tempus vitae. Lorem ipsum dolor sit amet, consectetur adipiscing elit. Fusce ultrices tempus pellentesque. Sed congue euismod urna a dignissim. Cras quis metus nec tortor pretium vehicula. Sed vel convallis enim, id luctus dolor. Quisque dui quam, sollicitudin ut neque vitae, fringilla luctus magna.</p>
</section>

<div class="rainbow" style="top:610px"><span class="o"></span><span class="r"></span><span class="p"></span><span class="y"></span><span class="g"></span><span class="b"></span></div>

<footer class="site-footer">
  <div class="foot-col nav"><h4>NAVIGATION</h4>Directory<br>Special Offers<br>Contact Us</div>
  <div class="foot-divider" style="left:375px"></div>
  <div class="foot-col contact"><h4>CONTACT</h4>PO Box 4410<br>Millbrook, CT<br>06000</div>
  <div class="foot-divider" style="left:565px"></div>
  <div class="foot-col legal"><h4>LEGAL</h4>Pendrelle © 2015<br>website design<br>by pendrelle-web.net</div>
  <div class="foot-brand"><span class="dot"></span>LedgerLocate</div>
</footer>

<p class="copyright">www.ledgerlocate.com © All Rights Reserved.</p>
</body>
</html>
```